Studying Effectively To Do List

I am looking to design a new "Study To Do List" for High School students (Ages 15 - 18) . This will be printed as an A4 notepad and so should only be a single A4 page.

The Design will need to be professional and look semi-serious but also be appealing to High school students (Ages 15 - 18) and should NOT be gender specific.

I have attached a word document outlining the structure of the page. The space provided should be large enough that people can write in it comfortably.

The notepad will most likely be printed in black and white but I'm also looking at coloured options - colours should be kept to a minimum.

This will be printed professionally and should also include a 3mm bleed.

The design should also include the business logo (included in the word document)

Target Market(s)

High School students (Ages 15 - 18). Both genders

Industry/Entity Type

Education

Font styles to use
Serif
Sans Serif

Requirements
Must have
• Please see the word document attached.
Should not have
• Too much colour

```html
<!DOCTYPE html>
<html lang="en">
<head>
<meta charset="utf-8">
<title>Study To Do List</title>
<link href="https://fonts.googleapis.com/css2?family=Montserrat:wght@400;500;800;900&display=swap" rel="stylesheet">
<style>
  :root {
    --canvas: #ececec;
    --paper: #ffffff;
    --slate: #37495a;
    --navy: #1f3347;
    --orange: #f18e2c;
    --panel: #f6f6f6;
    --rule: #a3a9af;
    --label: #34495c;
    --footer-text: #b9c3cc;
  }
  * { box-sizing: border-box; margin: 0; padding: 0; }
  html, body { width: 1200px; height: 1200px; overflow: hidden; }
  body {
    background: var(--canvas);
    font-family: "Montserrat", Arial, sans-serif;
    color: var(--label);
    position: relative;
  }
  .sheet {
    position: absolute;
    left: 196px; top: 29px;
    width: 808px; height: 1142px;
    background: linear-gradient(to bottom, var(--paper) 0%, var(--paper) 13%, #d3d7db 27%, #7d8a96 42%, var(--slate) 56%, var(--slate) 100%);
    padding: 22px 36px 0;
    display: flex; flex-direction: column; gap: 12px;
    box-shadow: 0 6px 24px rgba(0,0,0,.18);
  }
  .sheet-header {
    height: 92px;
    display: flex; align-items: center; justify-content: space-between;
  }
  .brand { display: flex; align-items: center; gap: 10px; }
  .brand-dot { width: 34px; height: 34px; border-radius: 50%; background: var(--orange); }
  .brand-name { font-weight: 800; font-size: 24px; color: var(--navy); }
  .date-field { display: flex; align-items: flex-end; gap: 10px; width: 300px; }
  .date-field span { font-weight: 900; font-size: 17px; color: var(--navy); }
  .date-field i { flex: 1; border-bottom: 1px solid var(--rule); height: 18px; }
  .panel {
    background: var(--panel);
    border-radius: 12px;
    padding: 12px 20px 14px;
  }
  .panel--outlined { border: 1px solid var(--orange); }
  .panel-title {
    font-weight: 900; font-size: 18px; color: var(--navy);
    text-transform: uppercase; letter-spacing: .3px; margin-bottom: 6px;
  }
  .row { display: flex; align-items: flex-end; height: 23px; font-size: 12px; gap: 8px; }
  .row .label { white-space: nowrap; }
  .row .rule { flex: 1; border-bottom: 1px solid var(--rule); height: 14px; }
  .cols { display: grid; grid-template-columns: 1fr 1fr; column-gap: 28px; }
  .row--num .label { width: 16px; }
  .row--indent .label { padding-left: 6px; }
  .row--due .due { margin-left: 14px; }
  .bottom { display: grid; grid-template-columns: 1fr 1fr; gap: 0; }
  .bottom .panel { border-radius: 12px; }
  .notes { border-radius: 12px 0 0 12px !important; border-right: 1px solid var(--orange); }
  .practice { border-radius: 0 12px 12px 0 !important; }
  .practice .panel-title { text-align: right; }
  .sheet-footer {
    margin-top: auto; height: 34px;
    display: flex; align-items: center; justify-content: center;
    font-size: 12px; letter-spacing: .5px; color: var(--footer-text);
  }
</style>
</head>
<body>
<main class="sheet">
  <header class="sheet-header">
    <div class="brand"><div class="brand-dot"></div><div class="brand-name">Northpath</div></div>
    <div class="date-field"><span>DATE:</span><i></i></div>
  </header>

  <section class="panel panel--outlined revision">
    <h2 class="panel-title">Revision</h2>
    <div class="cols">
      <div>
        <div class="row row--num"><span class="label">1.</span><span class="rule"></span></div>
        <div class="row row--num"><span class="label">2.</span><span class="rule"></span></div>
        <div class="row row--num"><span class="label">3.</span><span class="rule"></span></div>
        <div class="row row--num"><span class="label">4.</span><span class="rule"></span></div>
      </div>
      <div>
        <div class="row row--num"><span class="label">5.</span><span class="rule"></span></div>
        <div class="row row--num"><span class="label">6.</span><span class="rule"></span></div>
        <div class="row row--num"><span class="label">7.</span><span class="rule"></span></div>
        <div class="row row--num"><span class="label">8.</span><span class="rule"></span></div>
      </div>
    </div>
  </section>

  <section class="panel homework">
    <h2 class="panel-title">Homework</h2>
    <div class="row"><span class="label">Subject</span><span class="rule"></span></div>
    <div class="row row--indent"><span class="label">Task</span><span class="rule"></span></div>
    <div class="row"><span class="label">Subject</span><span class="rule"></span></div>
    <div class="row row--indent"><span class="label">Task</span><span class="rule"></span></div>
    <div class="row"><span class="label">Subject</span><span class="rule"></span></div>
    <div class="row row--indent"><span class="label">Task</span><span class="rule"></span></div>
    <div class="row"><span class="label">Subject</span><span class="rule"></span></div>
    <div class="row row--indent"><span class="label">Task</span><span class="rule"></span></div>
    <div class="row"><span class="label">Subject</span><span class="rule"></span></div>
    <div class="row row--indent"><span class="label">Task</span><span class="rule"></span></div>
    <div class="row"><span class="label">Subject</span><span class="rule"></span></div>
    <div class="row row--indent"><span class="label">Task</span><span class="rule"></span></div>
  </section>

  <section class="panel assessments">
    <h2 class="panel-title">Assessments</h2>
    <div class="row row--due"><span class="label">Assessment:</span><span class="rule"></span><span class="label due">Due</span><span class="rule"></span></div>
    <div class="row row--indent"><span class="label">Element:</span><span class="rule"></span></div>
    <div class="row row--due"><span class="label">Assessment:</span><span class="rule"></span><span class="label due">Due</span><span class="rule"></span></div>
    <div class="row row--indent"><span class="label">Element:</span><span class="rule"></span></div>
    <div class="row row--due"><span class="label">Assessment:</span><span class="rule"></span><span class="label due">Due</span><span class="rule"></span></div>
    <div class="row row--indent"><span class="label">Element:</span><span class="rule"></span></div>
    <div class="row row--due"><span class="label">Assessment:</span><span class="rule"></span><span class="label due">Due</span><span class="rule"></span></div>
    <div class="row row--indent"><span class="label">Element:</span><span class="rule"></span></div>
    <div class="row row--due"><span class="label">Assessment:</span><span class="rule"></span><span class="label due">Due</span><span class="rule"></span></div>
    <div class="row row--indent"><span class="label">Element:</span><span class="rule"></span></div>
    <div class="row row--due"><span class="label">Assessment:</span><span class="rule"></span><span class="label due">Due</span><span class="rule"></span></div>
    <div class="row row--indent"><span class="label">Element:</span><span class="rule"></span></div>
  </section>

  <div class="bottom">
    <section class="panel notes">
      <h2 class="panel-title">Notes</h2>
      <div class="cols">
        <div>
          <div class="row row--num"><span class="label">1.</span><span class="rule"></span></div>
          <div class="row row--num"><span class="label">2.</span><span class="rule"></span></div>
          <div class="row row--num"><span class="label">3.</span><span class="rule"></span></div>
          <div class="row row--num"><span class="label">4.</span><span class="rule"></span></div>
        </div>
        <div>
          <div class="row row--num"><span class="label">5.</span><span class="rule"></span></div>
          <div class="row row--num"><span class="label">6.</span><span class="rule"></span></div>
          <div class="row row--num"><span class="label">7.</span><span class="rule"></span></div>
          <div class="row row--num"><span class="label">8.</span><span class="rule"></span></div>
        </div>
      </div>
    </section>
    <section class="panel practice">
      <h2 class="panel-title">Practice</h2>
      <div class="row row--num"><span class="label">1.</span><span class="rule"></span></div>
      <div class="row row--num"><span class="label">2.</span><span class="rule"></span></div>
      <div class="row row--num"><span class="label">3.</span><span class="rule"></span></div>
      <div class="row row--num"><span class="label">4.</span><span class="rule"></span></div>
    </section>
  </div>

  <footer class="sheet-footer">northpathstudy.com.au</footer>
</main>
</body>
</html>
```